Medical Device Packaging Project 3 of 5

We are a medical device startup company needing packaging for a total of 5 device brands. This is posting 3 of 5 and the device name is "Venor"

Venor is an intraocular lens for use in cataract surgery. The target market is Chinese ophthalmologists. The box should be sophisticated and upmarket.

The company name is Tamsin Medica, I have included the logo in the uploaded files section. You should include the logo on the box.

I have uploaded a sample lens boxes from other companies that demonstrate the information needed to be contained on the box in terms of address, warnings, symbols, etc.

I have also uploaded the blank dieline of the boxes

You are welcome and encouraged to also submit to projects 1, 2, 4, and 5 as well. The same rules and expectations apply.

Requirements
Should not have
• Should not have any images of an eye or any bionic/futuristic feel to the design
• Note that the calvoptix box is for text reference only. You may use the lens image but the futuristic/bionic look is NOT what we are going for with this brand. It should be traditional upmarket medical device artwork.

```html
<!DOCTYPE html>
<html lang="en">
<head>
<meta charset="utf-8">
<title>Venor – Intraocular Lens Carton Dieline</title>
<link href="https://fonts.googleapis.com/css2?family=Arimo:wght@400;700&family=Tinos&display=swap" rel="stylesheet">
<style>
:root{
  --paper:#ffffff;
  --carton:#58585a;
  --ink-light:#ffffff;
  --ink-muted:#e6e9eb;
  --rule:#8a8c8f;
  --dim:#2b2b2b;
  --bokeh-a:#d5dee3;
  --bokeh-b:#9fb2bc;
  --bokeh-c:#7f939e;
}
*{margin:0;padding:0;box-sizing:border-box}
html,body{width:1065px;height:1200px;overflow:hidden;background:var(--paper)}
.canvas{position:relative;width:1065px;height:1200px;font-family:"Arimo",Arial,sans-serif;color:var(--ink-light)}
.dieline{position:absolute;inset:0}
.dim{position:absolute;font-family:"Tinos","Times New Roman",serif;font-size:15px;color:var(--dim);white-space:nowrap}
.dim.vertical{transform:rotate(-90deg);transform-origin:center}
.abs{position:absolute}
.brand-name{font-family:"Arimo",Arial,sans-serif;font-weight:400;font-size:19px;letter-spacing:2px;color:var(--ink-light);white-space:nowrap;display:flex;align-items:center;justify-content:center;gap:7px}
.brand-name .dot{width:9px;height:9px;border-radius:50%;background:var(--ink-light);display:inline-block}
.brand-name.centered{width:246px;left:418px}
.brand-name.side{width:200px;height:24px;left:780px;top:458px;transform:rotate(-90deg);transform-origin:center}
.product-name{font-weight:700;color:var(--ink-light);letter-spacing:1px}
.lens-art{position:absolute;border-radius:50%;background:radial-gradient(circle at 40% 40%,#e8eef2 0%,#c3d0d8 60%,#a9bac4 100%)}
.contact{position:absolute;left:360px;top:140px;width:430px;transform:rotate(180deg);font-size:11px;font-weight:700;line-height:14px;text-align:left}
.tagline{position:absolute;left:480px;top:536px;font-size:11px;line-height:13px;text-align:right;border-bottom:1px solid var(--ink-light);padding-bottom:3px}
.feature{position:absolute;left:290px;top:606px;font-size:14px;font-weight:700}
.info-panel{position:absolute;left:317px;top:758px;width:446px;height:322px;background:var(--carton)}
.info-divider{position:absolute;left:228px;top:12px;width:1px;height:298px;background:var(--rule)}
.info-text{position:absolute;left:246px;top:10px;width:196px;font-size:7.9px;line-height:9px;color:var(--ink-muted);white-space:nowrap}
.info-text p{margin-bottom:6px}
.info-text p.greek{font-size:6.8px;line-height:8.2px}
</style>
</head>
<body>
<div class="canvas">

  <svg class="dieline" width="1065" height="1200" viewBox="0 0 1065 1200" aria-hidden="true">
    <defs>
      <linearGradient id="bokeh" x1="0" y1="0" x2="1" y2="1">
        <stop offset="0" stop-color="var(--bokeh-b)"/>
        <stop offset="0.45" stop-color="var(--bokeh-a)"/>
        <stop offset="1" stop-color="var(--bokeh-c)"/>
      </linearGradient>
    </defs>
    <polygon points="148,92 273,64 808,64 955,92 955,190 148,190" fill="var(--carton)"/>
    <path d="M273,210 H74 Q52,210 52,232 V561 Q52,583 74,583 H273 Z" fill="var(--carton)"/>
    <rect x="273" y="210" width="535" height="373" fill="var(--carton)"/>
    <rect x="273" y="210" width="145" height="373" fill="url(#bokeh)" role="img" aria-label="Soft blue-grey bokeh light background"/>
    <rect x="664" y="210" width="144" height="373" fill="url(#bokeh)" role="img" aria-label="Soft blue-grey bokeh light background"/>
    <path d="M808,210 H1006 Q1028,210 1028,232 V561 Q1028,583 1006,583 H808 Z" fill="var(--carton)"/>
    <polygon points="148,601 955,601 955,690 808,718 273,718 148,690" fill="var(--carton)"/>
    <rect x="273" y="731" width="535" height="377" fill="url(#bokeh)" role="img" aria-label="Soft blue-grey bokeh light background"/>
    <path d="M273,1108 H808 L800,1172 Q799,1180 790,1180 H290 Q281,1180 280,1172 Z" fill="var(--carton)"/>
  </svg>

  <span class="dim" style="left:195px;top:33px">35mm</span>
  <span class="dim" style="left:497px;top:39px">128mm</span>
  <span class="dim" style="left:848px;top:33px">35mm</span>
  <span class="dim vertical" style="left:102px;top:130px">35mm</span>
  <span class="dim" style="left:68px;top:174px">18mm</span>
  <span class="dim" style="left:972px;top:174px">18mm</span>
  <span class="dim vertical" style="left:14px;top:381px">90mm</span>
  <span class="dim vertical" style="left:102px;top:636px">35mm</span>
  <span class="dim vertical" style="left:212px;top:921px">90mm</span>
  <span class="dim vertical" style="left:214px;top:1131px">12mm</span>

  <div class="contact">
    website: www.tamsinmedica.net &nbsp;email: info@tamsinmedica.net<br>
    Full company address and contact<br>
    details will be placed here later
  </div>

  <div class="brand-name centered abs" style="top:272px"><span class="dot"></span>TAMSIN MEDICA</div>
  <div class="lens-art" style="left:468px;top:345px;width:150px;height:150px" role="img" aria-label="Intraocular lens with curved haptics"></div>
  <div class="product-name abs" style="left:482px;top:494px;font-size:36px">VENOR</div>
  <div class="tagline"><b>Intraocular lens</b> for use<br>in cataract surgery</div>

  <svg class="abs" style="left:906px;top:222px" width="30" height="170" viewBox="0 0 30 170" aria-label="Regulatory symbols" role="img">
    <g fill="none" stroke="#fff" stroke-width="1.2">
      <circle cx="15" cy="12" r="7"/><line x1="10" y1="7" x2="20" y2="17"/>
      <circle cx="15" cy="42" r="7"/><line x1="10" y1="37" x2="20" y2="47"/>
      <circle cx="15" cy="70" r="7"/>
      <polygon points="8,104 15,91 22,104"/>
      <rect x="9" y="122" width="12" height="40"/><line x1="9" y1="136" x2="21" y2="136"/>
    </g>
    <text x="15" y="74" fill="#fff" font-size="9" text-anchor="middle" font-family="Arimo">2</text>
  </svg>
  <div class="brand-name side abs"><span class="dot"></span>TAMSIN MEDICA</div>

  <div class="feature">WITH 360° SQUARE EDGE</div>
  <div class="brand-name centered abs" style="top:650px"><span class="dot"></span>TAMSIN MEDICA</div>

  <div class="info-panel">
    <div class="product-name abs" style="left:67px;top:12px;font-size:30px">VENOR</div>
    <div class="lens-art" style="left:48px;top:88px;width:140px;height:140px" role="img" aria-label="Intraocular lens with curved haptics"></div>
    <div class="info-divider"></div>
    <div class="info-text">
      <p>Contains one sterile intraocular lens<br>Do not use if the packaging is damaged<br>Do not resterilize</p>
      <p>Bevat één steriele intraoculaire lens<br>Niet gebruiken als de verpakking beschadigd is<br>Niet opnieuw steriliseren</p>
      <p>Contient une lentille intraoculaire stérile<br>Ne pas utiliser si l'emballage est endommagé<br>Ne pas restériliser</p>
      <p>Enthält eine sterile intraokulare Linse<br>Nicht verwenden, wenn die Verpackung beschädigt ist<br>Nicht resterilisieren</p>
      <p class="greek">Periéchei éna aposteiroméno endofthálmia fakó OR<br>Περιέχει ένα αποστειρωμένο ενδοφθάλμια φακό<br>Μην το χρησιμοποιείτε εάν η συσκευασία έχει υποστεί ζημιά<br>OR Min to chrisimopoieíte eán i syskevasía échei ypostei zimiá<br>Μην επαναποστειρώνετε OR Min epanaposteirónete</p>
      <p>Contiene una lente intraoculare sterile<br>Non usare se la confezione è danneggiata<br>Non risterilizzare</p>
      <p>Contém uma lente intra-ocular esterilizada<br>Não use se a embalagem está danificada<br>Não reesterilize</p>
      <p>Contiene una lente intraocular estéril<br>No utilizar si el envase está dañado<br>No vuelva a esterilizar</p>
    </div>
    <svg class="abs" style="left:246px;top:290px" width="180" height="20" viewBox="0 0 180 20" aria-label="Regulatory symbols" role="img">
      <g fill="none" stroke="#fff" stroke-width="1">
        <rect x="0.5" y="2" width="44" height="15"/><line x1="32" y1="2" x2="32" y2="17"/>
        <polygon points="56,17 64,3 72,17"/>
        <circle cx="94" cy="10" r="7"/>
        <circle cx="124" cy="10" r="7"/><line x1="119" y1="5" x2="129" y2="15"/>
        <circle cx="154" cy="10" r="7"/><line x1="149" y1="5" x2="159" y2="15"/>
      </g>
      <g fill="#fff" font-family="Arimo" font-size="6.5">
        <text x="3" y="12">STERILE</text><text x="34" y="12">EO</text>
        <text x="91.5" y="13" font-size="9">2</text>
      </g>
    </svg>
  </div>

</div>
</body>
</html>
```